Brochure Design Project

Using supplied logo and supplied graphics I want a 4-page brochure 81/2x 11" that can be used as a leave behind, a self mailer and a pdf email attachment for promotion purposes.
The cover needs to be visually provocative and support the following questions"
"Have you lost your leadership edge... has your company lost it's momentum... are your employees as engaged as they need to be?"
The inside of the brochure should explain the Amber Ridge Coaching 7 Step process with is explained in the attached PowerPoint.
Back page should be brief bio of me. And Statement about who we work with. I am attaching a tri-fold brochure we designed but do not like because it is bland and the graphic inside is hard to read.
Target Market(s)
"C" level executives (CEO, CIO, CFO, CMO, CRO etc)
Industry/Entity Type
Leadership
Look and feel

```html
<!DOCTYPE html>
<html lang="en">
<head>
<meta charset="utf-8">
<title>Step 4: Achieve Common View and Alignment</title>
<link rel="stylesheet" href="https://fonts.googleapis.com/css2?family=Sorts+Mill+Goudy&display=swap">
<style>
  :root {
    --band-blue: #0b6fd0;
    --band-blue-light: #2a8ee6;
    --band-edge: #0a4a8c;
    --label-blue: #1a80d6;
    --body-text: #4d4d4d;
    --bullet-blue: #1a72cc;
    --page: #ffffff;
    --photo-light: #f1f2f4;
    --photo-mid: #dfe2e6;
  }
  * { margin: 0; padding: 0; box-sizing: border-box; }
  html, body { width: 927px; height: 1200px; overflow: hidden; background: var(--page); }
  .page {
    position: relative;
    width: 927px;
    height: 1200px;
    background: var(--page);
    font-family: "Sorts Mill Goudy", "Goudy Bookletter 1911", Georgia, serif;
    color: var(--body-text);
  }
  .title-band {
    position: absolute;
    left: 0; top: 129px;
    width: 927px; height: 280px;
    background: radial-gradient(ellipse at 20% 30%, var(--band-blue-light) 0%, var(--band-blue) 55%, #0862bd 100%);
    border-top: 10px solid var(--band-edge);
    border-bottom: 12px solid var(--band-edge);
    display: flex;
    align-items: center;
    justify-content: center;
  }
  .title-band h1 {
    margin-left: 70px;
    width: 860px;
    font-weight: 400;
    font-size: 46px;
    line-height: 71px;
    color: #ffffff;
    text-align: center;
  }
  .goal-label {
    position: absolute;
    left: 0; top: 504px;
    width: 424px; height: 60px;
    background: var(--label-blue);
    color: #ffffff;
    font-size: 38px;
    line-height: 60px;
    padding-left: 61px;
  }
  .goal-list {
    position: absolute;
    left: 61px; top: 576px;
    width: 430px;
    list-style: none;
  }
  .goal-list li {
    position: relative;
    font-size: 40px;
    line-height: 72.5px;
  }
  .goal-list li::before {
    content: "";
    position: absolute;
    left: -29px; top: 30px;
    width: 15px; height: 15px;
    border-radius: 50%;
    background: var(--bullet-blue);
  }
  .alignment-photo {
    position: absolute;
    left: 467px; top: 462px;
    width: 460px; height: 405px;
    background: linear-gradient(135deg, var(--photo-light) 0%, var(--photo-mid) 100%);
    box-shadow: -4px 6px 12px rgba(0,0,0,0.25);
  }
  .footer-band {
    position: absolute;
    left: 0; top: 1118px;
    width: 927px; height: 82px;
    background: linear-gradient(180deg, var(--band-blue) 0%, var(--band-blue-light) 100%);
    border-top: 10px solid var(--band-edge);
  }
</style>
</head>
<body>
  <main class="page">
    <header class="title-band">
      <h1>STEP #4: Achieve Common View and<br>Alignment</h1>
    </header>

    <div class="goal-label">GOAL:</div>
    <ul class="goal-list">
      <li>Attain consensus view<br>of situation</li>
      <li>Align Personal and<br>organizational beliefs<br>and values</li>
      <li>Begin to consider initial<br>steps forward</li>
    </ul>

    <div class="alignment-photo" role="img" aria-label="Photo of a whiteboard sketch titled Goal Alignment Strategy, with red boxes for corporate, business unit, team and individual goals joined by blue arrows toward a Success box, beside a ruler, pen and sticky notes"></div>

    <footer class="footer-band"></footer>
  </main>
</body>
</html>
```